Corwin Ashgrove

I am a songwriter and would like to include a bio, pictures, discography, CD covers and access to some of my music

Target Market(s)

Music Lovers, songwriters publishers

Coding

Coded - Design and coding required

Number of Pages Required

5+ page

Requirements
Must have
• Pictures of my CD covers, pictures of me and either my Music or links to my music
Nice to have
Should not have
• cartoons

```html
<!DOCTYPE html>
<html lang="en">
<head>
<meta charset="utf-8">
<title>Corwin Ashgrove – Songwriter</title>
<link href="https://fonts.googleapis.com/css2?family=Titillium+Web:wght@400;600;700&family=Open+Sans:wght@400;600&family=Oswald:wght@500&display=swap" rel="stylesheet">
<style>
:root{
  --black:#000;
  --footer:#1b1b1b;
  --white:#fff;
  --red:#e8262b;
  --orange:#e8892a;
  --crimson:#c0193f;
  --yellow:#fdbd45;
  --gold:#f2b418;
  --text-grey:#d9d9d9;
  --dark:#1c1c1c;
}
*{margin:0;padding:0;box-sizing:border-box}
html,body{width:1200px;height:4717px;overflow:hidden;background:var(--black)}
body{font-family:"Open Sans",sans-serif;color:var(--white);position:relative}
section,header,footer{position:absolute;left:0;width:1200px}
.abs{position:absolute}
.heading{font-family:"Titillium Web",sans-serif;font-weight:700;text-align:center;width:100%}

/* hero */
.hero{top:0;height:825px;background:radial-gradient(ellipse 520px 420px at 820px 380px,#b8620c 0%,#5a2a06 45%,#140700 80%),#000}
.nav{top:56px;right:115px;display:flex;gap:30px;font-family:"Titillium Web",sans-serif;font-weight:700;font-size:14px}
.nav-tab{left:490px;top:0;width:86px;height:94px;background:#7d6a12;border-radius:0 0 16px 16px}
.brand-small{left:115px;top:32px;font-family:"Titillium Web",sans-serif;font-weight:700;font-size:30px;color:var(--gold);line-height:1}
.hero-photo{left:690px;top:150px;width:450px;height:675px;background:radial-gradient(ellipse at 50% 40%,#e9dcc9 0%,#8c6a4a 45%,rgba(60,30,10,0) 75%)}
.hero-bars{left:0;top:440px;width:560px;height:200px;background:linear-gradient(90deg,rgba(200,30,0,0),rgba(220,40,0,.55) 30%,rgba(220,40,0,.2));opacity:.6}
.brand-large{left:110px;top:320px;font-family:"Titillium Web",sans-serif;font-weight:700;font-size:80px;color:var(--gold);line-height:.95}
.tagline{left:288px;top:492px;font-family:"Titillium Web",sans-serif;font-weight:700;font-size:38px}

/* about */
.about{top:825px;height:641px;background:var(--black)}
.about-glow{left:62px;top:65px;width:350px;height:350px;border-radius:50%;background:#3a1106}
.about-photo{left:187px;top:140px;width:432px;height:432px;border-radius:50%;background:radial-gradient(circle at 55% 45%,#c9b7a4,#6c7d93 60%,#3b3b3b)}
.about h2{left:614px;top:118px;font-family:"Titillium Web",sans-serif;font-weight:700;font-size:58px;letter-spacing:5px;line-height:1}
.about p{left:614px;top:197px;width:470px;font-size:14px;line-height:22.3px;text-align:justify;color:var(--text-grey)}
.btn-read{left:614px;top:510px;width:168px;height:48px;border-radius:24px;background:var(--red);font-family:"Titillium Web",sans-serif;font-weight:700;font-size:16px;display:flex;align-items:center;justify-content:center}

/* reviews */
.reviews{top:1466px;height:687px;background:linear-gradient(180deg,var(--orange) 0%,#d9522f 45%,var(--crimson) 100%)}
.reviews .heading{top:76px;font-size:38px}
.intro{width:760px;left:220px;text-align:center;font-size:14px;line-height:22px}
.review-card{top:259px;width:444px;height:343px;border:2px solid var(--white);border-radius:12px}
.quote{top:270px;font-family:Georgia,serif;font-size:110px;line-height:1;font-weight:700}
.review-text{left:43px;top:38px;width:370px;font-family:"Titillium Web",sans-serif;font-size:15.5px;line-height:26.7px}
.reviewer{left:43px;top:248px;font-family:"Titillium Web",sans-serif;font-size:17px}
.stars{left:43px;top:287px;color:#ffd21f;font-size:17px;letter-spacing:1px}
.arrow{top:380px}

/* cd covers */
.covers{top:2153px;height:577px;background:var(--black)}
.covers .heading{top:78px;font-size:36px}
.cover{top:152px;width:313px}
.cover-art{width:313px;height:202px;background:var(--white);padding:10px}
.cover-art div{width:100%;height:100%}
.date{left:10px;top:220px;width:38px;height:40px;background:var(--red);font-family:"Oswald",sans-serif;font-size:11px;line-height:14px;text-align:center;padding-top:5px}
.cover h3{left:66px;top:218px;font-family:"Oswald",sans-serif;font-weight:500;font-size:20px;white-space:nowrap}
.cover p{left:66px;top:250px;width:245px;font-size:14px;line-height:25px;color:var(--text-grey)}
.cover a{left:66px;top:333px;font-family:"Oswald",sans-serif;font-size:12px;color:var(--red)}

/* music */
.music{top:2730px;height:595px;background:var(--yellow)}
.music .heading{top:78px;font-size:60px;letter-spacing:5px;color:var(--dark)}
.music .intro{top:172px;color:#6a4a1a}
.track{width:428px;height:52px;background:var(--white);border-radius:4px;display:flex;align-items:center;padding:0 14px;font-size:15px;color:#555}
.track .time{margin-left:auto;margin-right:20px;font-size:13px;color:#777}

/* discography */
.disco{top:3325px;height:870px;background:var(--black)}
.disco .heading{top:78px;font-size:36px}
.disco .intro{top:137px;font-size:15px;line-height:28px}
.disc{width:315px;height:277px}

/* footer */
.site-footer{top:4195px;height:522px;background:var(--footer)}
.site-footer h4{font-family:"Titillium Web",sans-serif;font-weight:700;font-size:23px;top:62px}
.rule{top:120px;width:66px;height:3px;background:var(--gold)}
.field{height:34px;border:1px solid #777;font-size:12px;padding:9px 12px}
.btn-submit{left:112px;top:362px;width:188px;height:42px;background:var(--red);font-family:"Titillium Web",sans-serif;font-weight:700;font-size:15px;display:flex;align-items:center;justify-content:center}
.contact-item{left:627px;display:flex;gap:20px;font-size:14px;line-height:20px;color:var(--text-grey)}
.icon-ring{width:34px;height:34px;border:2px solid var(--gold);border-radius:50%;flex:none;display:flex;align-items:center;justify-content:center}
.links{left:933px;top:144px;list-style:none;font-size:14px;line-height:30px;color:var(--text-grey)}
.divider{left:112px;top:448px;width:976px;height:1px;background:#333}
.copyright{left:112px;top:480px;font-size:14px;color:var(--text-grey)}
.social{top:472px;width:34px;height:34px;border:2px solid var(--white);border-radius:50%}
</style>
</head>
<body>

<header class="hero">
  <div class="abs hero-bars"></div>
  <div class="abs hero-photo" role="img" aria-label="Portrait of the songwriter in a white shirt and dark jacket against golden stage lights"></div>
  <div class="abs nav-tab"></div>
  <div class="abs brand-small">Corwin<br>Ashgrove</div>
  <nav class="abs nav"><span>HOME</span><span>BIO</span><span>DISCOGRAPHY</span><span>GALLERY</span><span>REVIEWS</span><span>BLOG</span><span>CONTACT</span></nav>
  <div class="abs brand-large">Corwin<br>Ashgrove</div>
  <div class="abs tagline">songwriter</div>
</header>

<section class="about">
  <div class="abs about-glow"></div>
  <div class="abs about-photo" role="img" aria-label="The songwriter holding a tiger cub"></div>
  <h2 class="abs">ABOUT ME</h2>
  <p class="abs">Corwin Ashgrove was born and raised in Houston, Texas. He began playing music at the age of eight when his sister returned home from summer camp and asked her parents to buy her a baritone ukulele. She taught her younger brother some chords on the ukulele and he was hooked. The following spring, they went to one of the border towns in Mexico and bought a Mexican guitar for $12. They restrung it with nylon strings and Ashgrove began to learn how to play the guitar. He took guitar lessons at a local music store and learned how to play the hits of the day by groups like the Harbor Lights, the Foxgloves, and the Cartwheels. He got his first electric guitar when he was about 10 years old. He began jamming with other musicians when he was 13 or 14. They were much more experienced than he and introduced him to the blues.</p>
  <div class="abs btn-read">READ MORE</div>
</section>

<section class="reviews">
  <h2 class="abs heading">MY REVIEWS</h2>
  <p class="abs intro" style="top:160px">Sed ut perspiciatis unde omnis iste natus sit voluptatem accusantium doloremque laudantium, totam rem aperiam, eaque ipsa quae ab illo inventore veritatis et quasi architecto beatae vitae dicta sunt explicabo.</p>
  <svg class="abs arrow" style="left:58px" width="26" height="44" viewBox="0 0 26 44"><path d="M22 4 6 22l16 18" fill="none" stroke="#fff" stroke-width="5"/></svg>
  <svg class="abs arrow" style="left:1114px" width="26" height="44" viewBox="0 0 26 44"><path d="M4 4l16 18L4 40" fill="none" stroke="#fff" stroke-width="5"/></svg>
  <div class="abs quote" style="left:118px">“</div>
  <div class="abs review-card" style="left:143px">
    <p class="abs review-text">At this point I have developed a continuous creative relationship with Corwin and have recorded on approximately 30 songs of his. He writes well-structured songs that allow me to flex my creative muscles. Corwin knows how to make his original ideas blossom into fully constructed arrangements that sound great</p>
    <div class="abs reviewer">Lucas Ferreira, Lowline Studio Bass</div>
    <div class="abs stars">★★★★★</div>
  </div>
  <div class="abs quote" style="left:606px">“</div>
  <div class="abs review-card" style="left:632px">
    <p class="abs review-text">Corwin puts an all-star cast together to create crafted compositions. I'm glad to be a part of it. Corwin has a ton of great material and is producing it very well. Great music coming from Corwin. I have enjoyed all the projects I've worked on with him, He's producing a ton of great new music.</p>
    <div class="abs reviewer">Nolan Reyes Saxaphone</div>
    <div class="abs stars">★★★★★</div>
  </div>
</section>

<section class="covers">
  <h2 class="abs heading">MY CD COVERS</h2>
  <article class="abs cover" style="left:112px">
    <div class="cover-art"><div role="img" aria-label="Pastel CD cover with a child's photo, case and disc" style="background:linear-gradient(135deg,#f2ecc8,#d9c6e6 50%,#9fb1c9)"></div></div>
    <div class="abs date">OCT<br>30</div><h3 class="abs">CHILDHOOD WINDOWS</h3>
    <p class="abs">Lorem ipsum dolor sit amet, conse ctetur adipiscing elit, sed do eiusm od tempor incididunt.</p>
    <a class="abs"><u>Listen my music</u></a>
  </article>
  <article class="abs cover" style="left:444px">
    <div class="cover-art"><div role="img" aria-label="Bright CD cover of a guitarist, case and disc" style="background:linear-gradient(135deg,#e03a8c,#35b04a 45%,#3aa0d8)"></div></div>
    <div class="abs date">OCT<br>30</div><h3 class="abs">OLD PORCH STRINGS</h3>
    <p class="abs">Lorem ipsum dolor sit amet, conse ctetur adipiscing elit, sed do eiusm od tempor incididunt.</p>
    <a class="abs"><u>Listen my music</u></a>
  </article>
  <article class="abs cover" style="left:775px">
    <div class="cover-art"><div role="img" aria-label="Green forest CD covers and disc" style="background:linear-gradient(135deg,#0d2a0d,#2f7d2a 50%,#111)"></div></div>
    <div class="abs date">OCT<br>30</div><h3 class="abs">PINES AFTER RAIN</h3>
    <p class="abs">Lorem ipsum dolor sit amet, conse ctetur adipiscing elit, sed do eiusm od tempor incididunt.</p>
    <a class="abs"><u>Listen my music</u></a>
  </article>
</section>

<section class="music">
  <h2 class="abs heading">MY MUSIC</h2>
  <p class="abs intro">Sed ut perspiciatis unde omnis iste natus error sit voluptatem accus antium doloremque laudantium, totam rem aperiam, eaque ipsa quae ab illo inventore veritatis et quasi architecto beatae vitae dicta sunt explicabo. Nemo enim ipsam voluptatem quia voluptas sit aspernatur aut odit aut fugit</p>
  <svg width="0" height="0" style="position:absolute"><symbol id="note" viewBox="0 0 20 20"><path d="M6 3l12-2v13" fill="none" stroke="#555" stroke-width="2"/><path d="M6 3v13" stroke="#555" stroke-width="2"/><circle cx="4" cy="16" r="3" fill="#555"/><circle cx="16" cy="14" r="3" fill="#555"/></symbol></svg>
  <div class="abs track" style="left:170px;top:257px">Sed utpespic iatisunde<span class="time">4:35 min</span><svg width="22" height="22"><use href="#note"/></svg></div>
  <div class="abs track" style="left:170px;top:322px">Sed utpespic iatisunde<span class="time">4:35 min</span><svg width="22" height="22"><use href="#note"/></svg></div>
  <div class="abs track" style="left:170px;top:388px">Sed utpespic iatisunde<span class="time">4:35 min</span><svg width="22" height="22"><use href="#note"/></svg></div>
  <div class="abs track" style="left:170px;top:454px">Sed utpespic iatisunde<span class="time">4:35 min</span><svg width="22" height="22"><use href="#note"/></svg></div>
  <div class="abs track" style="left:615px;top:257px">Sed utpespic iatisunde<span class="time">4:35 min</span><svg width="22" height="22"><use href="#note"/></svg></div>
  <div class="abs track" style="left:615px;top:322px">Sed utpespic iatisunde<span class="time">4:35 min</span><svg width="22" height="22"><use href="#note"/></svg></div>
  <div class="abs track" style="left:615px;top:388px">Sed utpespic iatisunde<span class="time">4:35 min</span><svg width="22" height="22"><use href="#note"/></svg></div>
  <div class="abs track" style="left:615px;top:454px">Sed utpespic iatisunde<span class="time">4:35 min</span><svg width="22" height="22"><use href="#note"/></svg></div>
</section>

<section class="disco">
  <h2 class="abs heading">DISCOGRAPHY</h2>
  <p class="abs intro" style="left:330px;width:540px">Lorem ipsum dolor sit amet, consectetur adipiscing elit, sed do eiusmod tempor incididunt ut labore et dolore magna aliqua.</p>
  <div class="abs disc" style="left:112px;top:218px;background:linear-gradient(160deg,#5a5a7a,#2a2a3a 60%,#8a2a10)" role="img" aria-label="Album cover: stormy sky with lightning over a silhouetted figure"></div>
  <div class="abs disc" style="left:443px;top:218px;background:linear-gradient(180deg,#0a0a0a,#3a1a0a 45%,#f0f0f0 70%)" role="img" aria-label="Album cover: track listing beneath a fiery horizon"></div>
  <div class="abs disc" style="left:773px;top:218px;background:linear-gradient(135deg,#d8201a,#f2d21a 35%,#2a5ab8 65%,#1a1a1a)" role="img" aria-label="Album cover: colourful abstract painting"></div>
  <div class="abs disc" style="left:112px;top:510px;background:linear-gradient(135deg,#f4f0c8,#d8c6e8 50%,#a8bcd6)" role="img" aria-label="Album cover: pastel collage with a child's photo"></div>
  <div class="abs disc" style="left:443px;top:510px;background:linear-gradient(135deg,#d8409a,#8a3ac8 40%,#3ab0d8)" role="img" aria-label="Album cover: guitarist on a swirling psychedelic background"></div>
  <div class="abs disc" style="left:773px;top:510px;background:linear-gradient(180deg,#5a7aa8,#3a4a5a 45%,#1a2a3a)" role="img" aria-label="Album cover: stormy sea with crashing waves"></div>
</section>

<footer class="site-footer">
  <h4 class="abs" style="left:112px">REQUEST FOR QUOTATION</h4>
  <div class="abs rule" style="left:112px"></div>
  <div class="abs field" style="left:112px;top:162px;width:214px">First Name</div>
  <div class="abs field" style="left:343px;top:162px;width:214px">Last Name</div>
  <div class="abs field" style="left:112px;top:214px;width:214px">Phone Number</div>
  <div class="abs field" style="left:343px;top:214px;width:214px">Email Address</div>
  <div class="abs field" style="left:112px;top:266px;width:445px;height:68px">Message</div>
  <div class="abs btn-submit">SUBMIT</div>

  <h4 class="abs" style="left:627px">CONTACT US</h4>
  <div class="abs rule" style="left:627px"></div>
  <div class="abs contact-item" style="top:150px"><span class="icon-ring"><svg width="14" height="18" viewBox="0 0 14 18"><path d="M7 1a6 6 0 0 0-6 6c0 4 6 10 6 10s6-6 6-10a6 6 0 0 0-6-6z" fill="none" stroke="#f2b418" stroke-width="2"/><circle cx="7" cy="7" r="2" fill="#f2b418"/></svg></span><span>Corwin Ashgrove<br>304 enim ipsam voluptatem<br>quia voluptas sit</span></div>
  <div class="abs contact-item" style="top:237px"><span class="icon-ring"><svg width="16" height="16" viewBox="0 0 16 16"><path d="M3 1l3 3-2 2c1 2 4 5 6 6l2-2 3 3-2 2C7 15 1 9 1 3z" fill="#f2b418"/></svg></span><span>Phone :<br>555-0142-2777</span></div>
  <div class="abs contact-item" style="top:300px"><span class="icon-ring"><svg width="16" height="12" viewBox="0 0 16 12"><rect x="1" y="1" width="14" height="10" fill="none" stroke="#f2b418" stroke-width="1.6"/><path d="M1 1l7 6 7-6" fill="none" stroke="#f2b418" stroke-width="1.6"/></svg></span><span>E - Mail :<br>info@corwinashgrove.com</span></div>

  <h4 class="abs" style="left:933px">QUICK LINKS</h4>
  <div class="abs rule" style="left:933px"></div>
  <ul class="abs links"><li>Home</li><li>Bio</li><li>My music</li><li>Discography</li><li>Reviews</li><li>Contact Us</li></ul>

  <div class="abs divider"></div>
  <p class="abs copyright">© Copyright 2020 Corwin Ashgrove. All Rights Reserved.</p>
  <div class="abs social" style="left:963px"></div>
  <div class="abs social" style="left:1007px"></div>
  <div class="abs social" style="left:1051px"></div>
</footer>

</body>
</html>
```